In Search of a FANTASTIC BUSINESS CARD REFRESH AND REDESIGN

I would like to redesign the current business card for my company.  There is a parent company, Brookfane Care Group, with 2 operating companies - Brookfane Homecare and Brookfane Senior Living.
I will include the current business card design, along with the 3 logos I would like incorporated.  The business card can be two sided.  I'm looking for something clean, professional, and a fresh new look.

Target Market(s)
Hospitals, social workers, insurance agents, family members of seniors
Industry/Entity Type
Healthcare
Contact Information for Business Card
Name, title of person, address, phone number, web address, email address
Look and feel
Each slider illustrates characteristics of the customer's brand and the style your logo design should communicate.

```html
<!DOCTYPE html>
<html lang="en">
<head>
<meta charset="utf-8">
<title>Brookfane Homecare – Business Card</title>
<link rel="stylesheet" href="https://fonts.googleapis.com/css2?family=Raleway:wght@300;400;500&display=swap">
<style>
  :root {
    --backdrop: #ebebeb;
    --paper: #ffffff;
    --rose: #f38a91;
    --slate: #808080;
    --ink-grey: #7a7a7a;
    --card-shadow: 3px 4px 6px rgba(0, 0, 0, 0.28);
  }
  * { margin: 0; padding: 0; box-sizing: border-box; }
  html, body { width: 1200px; height: 1200px; overflow: hidden; }
  body {
    background: var(--backdrop);
    position: relative;
    font-family: "Raleway", sans-serif;
  }
  .card {
    position: absolute;
    left: 154px;
    width: 891px;
    height: 521px;
    background: var(--paper);
    box-shadow: var(--card-shadow);
    overflow: hidden;
  }
  .card--front { top: 54px; }
  .card--back { top: 629px; }
  .card__waves {
    position: absolute;
    inset: 0;
    width: 100%;
    height: 100%;
  }
  .wave--rose { fill: var(--rose); }
  .wave--slate { fill: var(--slate); }
  .wave--paper { fill: var(--paper); }

  .brand {
    position: absolute;
    width: 270px;
    display: flex;
    flex-direction: column;
    align-items: center;
  }
  .brand--front { left: 70px; top: 122px; }
  .brand--back { left: 546px; top: 229px; }
  .brand__mark {
    width: 90px;
    height: 78px;
    border-radius: 10px;
    background: var(--rose);
  }
  .brand__name {
    margin-top: 26px;
    color: var(--ink-grey);
    font-weight: 500;
    font-size: 38px;
    line-height: 1.05;
    text-align: center;
  }

  .holder {
    position: absolute;
    right: 60px;
    top: 206px;
    text-align: right;
    color: var(--paper);
  }
  .holder__name {
    font-size: 36px;
    font-weight: 400;
    letter-spacing: 0.5px;
    line-height: 1.1;
  }
  .holder__title {
    margin-top: 6px;
    font-size: 20px;
    font-weight: 300;
  }
  .contacts {
    position: absolute;
    right: 60px;
    top: 346px;
    list-style: none;
    color: var(--paper);
  }
  .contacts__item {
    display: flex;
    justify-content: flex-end;
    align-items: center;
    gap: 16px;
    height: 35px;
    font-size: 21px;
    font-weight: 300;
  }
  .contacts__icon { width: 17px; height: 17px; fill: var(--paper); }
</style>
</head>
<body>

<section class="card card--front" aria-label="Card front">
  <svg class="card__waves" viewBox="0 0 713 417" preserveAspectRatio="none" aria-hidden="true">
    <path class="wave--rose" d="M713 29 C620 25 560 60 500 130 C420 225 370 330 300 385 C250 420 130 425 0 377 L0 417 L713 417 Z"/>
  </svg>

  <div class="brand brand--front">
    <div class="brand__mark"></div>
    <p class="brand__name">Brookfane<br>Homecare</p>
  </div>

  <div class="holder">
    <h1 class="holder__name">DANA ROSS</h1>
    <p class="holder__title">Director</p>
  </div>

  <ul class="contacts">
    <li class="contacts__item">(000) 488-0000
      <svg class="contacts__icon" viewBox="0 0 24 24" aria-hidden="true"><path d="M6.6 10.8a15.1 15.1 0 0 0 6.6 6.6l2.2-2.2a1 1 0 0 1 1-.25 11.4 11.4 0 0 0 3.6.57 1 1 0 0 1 1 1V20a1 1 0 0 1-1 1A17 17 0 0 1 3 4a1 1 0 0 1 1-1h3.5a1 1 0 0 1 1 1c0 1.25.2 2.45.57 3.57a1 1 0 0 1-.25 1z"/></svg>
    </li>
    <li class="contacts__item">dana@brookfane.com
      <svg class="contacts__icon" viewBox="0 0 24 24" aria-hidden="true"><path d="M2 5h20v14H2z M3.5 6.5 12 13l8.5-6.5" stroke="#f38a91" stroke-width="1.4"/></svg>
    </li>
    <li class="contacts__item">www.brookfane.com
      <svg class="contacts__icon" viewBox="0 0 24 24" aria-hidden="true"><circle cx="12" cy="12" r="10"/><path d="M2 12h20M12 2c3 3 3 17 0 20M12 2c-3 3-3 17 0 20" fill="none" stroke="#f38a91" stroke-width="1.4"/></svg>
    </li>
  </ul>
</section>

<section class="card card--back" aria-label="Card back">
  <svg class="card__waves" viewBox="0 0 713 417" preserveAspectRatio="none" aria-hidden="true">
    <rect class="wave--slate" x="0" y="0" width="713" height="417"/>
    <path class="wave--rose" d="M713 42 C640 5 540 -5 470 5 C410 15 370 80 320 150 C250 250 160 375 0 388 L0 417 L713 417 Z"/>
    <path class="wave--paper" d="M713 97 C620 50 500 60 420 125 C360 175 320 240 260 300 C190 370 100 398 0 400 L0 417 L713 417 Z"/>
  </svg>

  <div class="brand brand--back">
    <div class="brand__mark"></div>
    <p class="brand__name">Brookfane<br>Homecare</p>
  </div>
</section>

</body>
</html>
```